IT services company needs a business card designed

-2 sided business card.-Front is going to be the logo raised (3D floating effect) on a black background. Make the logos spider web shiny silver and keep the spider the same design. -Back needs to have the following information:Doug Farrow, Managing Partner, Cell: 602-488-3179, Website: Kolvantra.com, Email: Doug@Kolvantra.com
Target Market(s)
IT Services
Industry/Entity Type
It Company
Contact Information for Business Card
-2 sided business card.
-Front is going to be the logo raised (3D floating effect) on a black background. Make the logos spider web shiny silver and keep the spider the same design.
-Back needs to have the following information:
Doug Farrow, Managing Partner, Cell: 602-488-3179, Website: Kolvantra.com, Email: Doug@Kolvantra.com
Look and feel

```html
<!DOCTYPE html>
<html lang="en">
<head>
<meta charset="utf-8">
<title>Kolvantra Business Card</title>
<link href="https://fonts.googleapis.com/css2?family=Poppins:wght@400;500&display=swap" rel="stylesheet">
<style>
  :root {
    --stage: #3a3b3d;
    --card-light: #ffffff;
    --card-light-shade: #ececec;
    --card-dark: #222324;
    --brand-blue: #1e9be0;
    --ink: #3c4650;
    --ink-dark: #1b1c1e;
    --silver: #c9ccd0;
  }
  * { box-sizing: border-box; margin: 0; padding: 0; }
  html, body {
    width: 1200px; height: 900px; overflow: hidden;
    background: var(--stage);
    font-family: "Poppins", sans-serif;
  }
  .canvas {
    width: 1200px; height: 900px;
    display: flex; flex-direction: column;
    align-items: center; justify-content: center; gap: 34px;
  }
  .card {
    position: relative;
    width: 700px; height: 400px;
    border-radius: 22px;
    overflow: hidden;
    box-shadow: 0 14px 34px rgba(0,0,0,.45);
  }

  /* back side: contact details */
  .card-back {
    background: radial-gradient(ellipse at 70% 30%, var(--card-light) 40%, var(--card-light-shade) 100%);
  }
  .holder-name {
    position: absolute; left: 44px; top: 150px;
    color: var(--brand-blue);
    font-size: 34px; font-weight: 500; letter-spacing: 2px;
    line-height: 1.2;
    text-transform: uppercase;
  }
  .holder-title {
    position: absolute; left: 44px; top: 198px;
    color: var(--ink); font-size: 17px; letter-spacing: .5px;
  }
  .divider {
    position: absolute; left: 44px; right: 44px; top: 238px;
    height: 2px; background: var(--brand-blue);
  }
  .contact {
    position: absolute; left: 44px; top: 256px;
    color: var(--ink); font-size: 14.5px; line-height: 30px;
  }
  .contact .label { color: var(--brand-blue); }

  .brand {
    position: absolute;
    display: flex; align-items: center;
  }
  .wordmark {
    font-weight: 500; line-height: 1;
  }
  .brand-dot {
    display: block; border-radius: 50%;
  }
  .card-back .brand {
    right: 44px; top: 176px; gap: 12px;
  }
  .card-back .wordmark {
    color: var(--ink-dark); font-size: 30px; letter-spacing: 4px;
  }
  .card-back .brand-dot {
    width: 12px; height: 12px; background: var(--brand-blue);
  }

  /* front side: name on black */
  .card-front {
    background: radial-gradient(ellipse at 50% 40%, #2c2d2f 0%, var(--card-dark) 70%);
  }
  .card-front .brand {
    left: 0; right: 0; top: 0; bottom: 0;
    flex-direction: column; justify-content: center; gap: 22px;
  }
  .card-front .wordmark {
    color: var(--silver); font-size: 48px; letter-spacing: 6px;
  }
  .card-front .brand-dot {
    width: 10px; height: 10px; background: var(--silver);
  }
</style>
</head>
<body>
<main class="canvas">
  <section class="card card-back">
    <h1 class="holder-name">Doug Farrow</h1>
    <p class="holder-title">Managing Partner</p>
    <div class="divider"></div>
    <div class="contact">
      <p><span class="label">Phone</span> : 602-488-3179 | <span class="label">Email</span> : Doug@Kolvantra.com | <span class="label">Web</span> : www.Kolvantra.com</p>
      <p><span class="label">Address</span> : 2871 Larkspur Lane Tempe, AZ 85281</p>
    </div>
    <div class="brand">
      <span class="brand-dot"></span>
      <p class="wordmark">KOLVANTRA</p>
    </div>
  </section>

  <section class="card card-front">
    <div class="brand">
      <p class="wordmark">KOLVANTRA</p>
      <span class="brand-dot"></span>
    </div>
  </section>
</main>
</body>
</html>
```